Veltrane Partners Website - developing a website for a new IIoT (Industrial Internet of Things) startup

Hi All-

Thought I'd re-write this bit...

Firstly, to everyone who has submitted designs, thank you.

Basically, we are looking for a simple/ elegant / modern website with clean lines and design. Because this is a startup, we don't have a great deal of content. Therefore, I'm relying on the site to give us an established / international feel (no images of London, London attractions, or the London skyline please!) We will have offices in London / LA and Tokyo by the end of this year.

Selecting great images is really important. As I say, abstract is fine (less literal.) Black and white is fine as well. We need to convey our expertise to new, international clients, so this is v.important.

http://www.pellucora41.it/ (favourite)
http://www.craftonvelmo.com/cases/

In terms of colour, I think white /grey/ black and maybe experiment with red for the word Veltrane and (possibly) Group. Please note** I need the following words / strap line written underneath the main logo: IIoT Strategy. Sensor Innovation. Machine Learning.

Whomever we chose to work with, this will be an ongoing partnership: we will continually need to add new content and update the site.

Thank you!

Tam.
Updates

**Please view updated brief description.

Target Market(s)

Mid-sized (£25M- £500M GBP) companies in the UK/ US and Asia. Facilities/ Construction/ Automotive/ Manufacturing / Engineering

Industry/Entity Type

Information Technology

Logo Text

Veltrane Partners -- IIoT Strategy. Sensor Innovation. Machine Learning (written underneath)

Coding

Coded - Design and coding required

Number of Pages Required

5+ page

Font styles to use
Sans Serif

Requirements
Must have
• An international, established, aspirational feel. Beautiful imagery. elegant infographics (nothing complex). CTA on homepage.
Should not have
• Anything cartoony / informal or naff corporate imagery.

```html
<!DOCTYPE html>
<html lang="en">
<head>
<meta charset="utf-8">
<title>Veltrane Partners – IIoT Strategy, Sensor Innovation, Machine Learning</title>
<link href="https://fonts.googleapis.com/css2?family=Open+Sans:wght@400;600;700;800&display=swap" rel="stylesheet">
<style>
:root{
  --red:#e2231a;
  --ink:#222;
  --text:#666;
  --grey-dark:#3b3b3b;
  --grey-deep:#2b2b2b;
  --grey-light:#ececec;
  --node:#4a4a4a;
  --white:#fff;
  --green:#2e6b3a;
}
*{margin:0;padding:0;box-sizing:border-box}
html,body{width:1200px;height:3814px;overflow:hidden}
body{font-family:"Open Sans",Arial,sans-serif;color:var(--ink);background:var(--white)}
.page{position:relative;width:1200px;height:3814px;overflow:hidden}

/* header / hero */
.hero{position:absolute;top:0;left:0;width:1200px;height:496px;
  background:linear-gradient(180deg,#5b6670 0%,#7d8a8c 35%,#6d7468 70%,#4d5a3e 100%)}
.hero-shade{position:absolute;inset:0;background:linear-gradient(180deg,rgba(0,0,0,.25),rgba(0,0,0,.35))}
.topbar{position:absolute;top:0;left:0;width:1200px;height:76px;background:rgba(20,20,20,.72)}
.brand{position:absolute;left:24px;top:8px;display:flex;align-items:center;gap:12px}
.brand-mark{width:18px;height:48px;background:var(--red)}
.brand-name{font-size:30px;font-weight:700;color:var(--white);line-height:1.1;white-space:nowrap}
.brand-tag{font-size:11px;color:#ddd;letter-spacing:.2px;white-space:nowrap}
.nav{position:absolute;left:389px;top:30px;display:flex;gap:30px;font-size:12px;font-weight:600;color:var(--white);letter-spacing:.5px}
.nav .active{border-bottom:2px solid var(--white);padding-bottom:3px}
.search-icon{position:absolute;left:874px;top:27px;width:22px;height:22px}
.search-box{position:absolute;left:966px;top:28px;width:128px;height:20px;border-radius:10px;background:var(--white)}
.hero h1{position:absolute;top:212px;width:1200px;text-align:center;font-size:46px;font-weight:700;color:var(--white)}
.hero-sub{position:absolute;top:282px;width:1200px;text-align:center;font-size:15px;color:#eee}

.btn{position:absolute;display:flex;align-items:center;justify-content:center;gap:18px;background:var(--red);color:var(--white);border-radius:30px;font-weight:700;text-transform:uppercase;letter-spacing:.5px}
.btn .arrow{width:26px;height:26px;border-radius:50%;background:var(--white);display:flex;align-items:center;justify-content:center}
.btn-hero{left:488px;top:343px;width:224px;height:51px;font-size:14px}
.btn-small{width:152px;height:41px;font-size:10px}
.btn-small .arrow{width:22px;height:22px}

/* section headings */
.sec-title{position:absolute;width:1200px;text-align:center;font-size:30px;font-weight:600}
.sec-rule{position:absolute;left:560px;width:80px;height:2px;background:var(--red)}

/* about */
.about{position:absolute;top:496px;left:0;width:1200px;height:414px;background:var(--white)}
.about p{position:absolute;left:230px;width:740px;text-align:center;font-size:13.5px;line-height:1.65;color:var(--text)}

/* strategy */
.strategy{position:absolute;top:910px;left:0;width:1200px;height:442px;
  background:linear-gradient(160deg,#3a3734 0%,#4e4a45 40%,#2f2d2a 100%);color:var(--white)}
.strategy p{position:absolute;left:265px;width:670px;text-align:center;font-size:12.5px;line-height:1.6;color:#eee}
.ideas{position:absolute;top:256px;width:1200px;text-align:center;font-size:19px;font-weight:700}
.idea{position:absolute;top:300px;width:234px;height:107px;border:1px solid rgba(255,255,255,.6);
  background:linear-gradient(135deg,#5a5650,#3c3a36);display:flex;align-items:center;justify-content:center;text-align:center;font-size:13.5px;line-height:1.3;padding:0 18px}

/* sensors */
.sensors{position:absolute;top:1352px;left:0;width:1200px;height:560px;background:linear-gradient(90deg,#f1f1f1,#e3e3e3)}
.sensors h2{position:absolute;left:100px;top:144px;font-size:24px;font-weight:600}
.sensors p{position:absolute;left:102px;top:186px;width:350px;font-size:13px;line-height:1.75;color:var(--text)}
.sensor-tree{position:absolute;left:0;top:0;width:1200px;height:560px}

/* data & ai */
.data{position:absolute;top:1912px;left:0;width:1200px;height:655px;
  background:linear-gradient(135deg,#4a4540 0%,#2d2b29 50%,#3d3a36 100%);color:var(--white)}
.data h2{position:absolute;top:112px;width:1200px;text-align:center;font-size:30px;font-weight:600}
.data p{position:absolute;top:162px;left:220px;width:760px;text-align:center;font-size:14px;line-height:1.6;color:#eee}
.pill{position:absolute;top:290px;width:184px;height:184px;border-radius:50%;border:9px solid var(--white);
  display:flex;align-items:center;justify-content:center;text-align:center;font-size:21px;font-weight:700;line-height:1.2;color:var(--white);background:var(--node);box-shadow:0 0 0 5px rgba(255,255,255,.25)}
.pill.red{background:var(--red)}
.outline-btn{position:absolute;left:466px;top:550px;width:267px;height:61px;border:2px solid rgba(255,255,255,.8);
  display:flex;align-items:center;justify-content:center;font-size:26px;color:var(--white)}

/* events */
.events{position:absolute;top:2567px;left:0;width:1200px;height:504px;background:var(--white)}
.kicker{position:absolute;font-size:14px;font-weight:700}
.big-label{position:absolute;font-size:30px;font-weight:700}
.event-photo{position:absolute;left:99px;top:102px;width:369px;height:351px;background:linear-gradient(160deg,#7a6648 0%,#3c3025 50%,#d8d2c6 100%)}
.event-head{position:absolute;left:534px;top:128px;font-size:16px;font-weight:700;letter-spacing:.5px}
.event-note{position:absolute;left:534px;top:152px;font-size:9px;color:#999;letter-spacing:.5px}
.cal{position:absolute;left:534px;top:186px;width:254px}
.cal-top{display:flex;justify-content:space-between;font-size:12px;font-weight:600;margin-bottom:10px}
.cal-top span.dots{color:#bbb;letter-spacing:8px}
.cal table{width:254px;border-collapse:collapse;font-size:9.5px;text-align:center;color:#555}
.cal th{background:#eee;font-weight:600;height:22px}
.cal td{height:28px;border-top:1px solid #eee}
.cal td.today span{display:inline-block;width:20px;height:20px;line-height:20px;border-radius:50%;background:var(--green);color:var(--white)}
.view-all{position:absolute;left:907px;top:134px;font-size:8.5px;font-weight:700;color:var(--green);letter-spacing:.5px}
.tree{position:absolute;left:930px;top:150px;width:170px;height:290px;border-radius:50% 50% 10px 10px;background:linear-gradient(180deg,rgba(120,150,160,.06),rgba(120,150,160,.14))}
.event-list{position:absolute;left:826px;top:177px;width:200px;list-style:none}
.event-list li{font-size:9.5px;font-weight:600;letter-spacing:.3px;margin-bottom:16px;color:#333}
.event-list small{display:block;font-size:7.5px;font-weight:700;color:var(--green);margin-top:3px}

/* blogs */
.blogs{position:absolute;top:3071px;left:0;width:1200px;height:386px;background:var(--grey-light)}
.card{position:absolute;top:99px;width:229px;height:236px;background:var(--white);box-shadow:0 2px 4px rgba(0,0,0,.08)}
.card-photo{height:147px}
.card time{display:block;font-size:8.5px;color:#888;margin:12px 10px 5px}
.card h3{font-size:12px;font-weight:700;line-height:1.3;margin:0 10px}

/* footer */
.footer{position:absolute;top:3457px;left:0;width:1200px;height:305px;background:var(--grey-dark);color:#ddd;border-top:3px solid var(--red)}
.foot-brand{position:absolute;left:24px;top:90px;width:300px;text-align:center}
.foot-brand .mark{width:26px;height:26px;background:var(--red);margin:0 auto 14px}
.foot-brand .name{font-size:28px;font-weight:600;color:var(--white);white-space:nowrap}
.foot-brand .tag{font-size:10.5px;color:#ccc;margin-top:4px;white-space:nowrap}
.foot-col{position:absolute;top:48px;font-size:11px;line-height:1.9}
.foot-col h4{font-size:13px;font-weight:700;color:var(--white);margin-bottom:4px}
.contact-row{display:flex;align-items:flex-start;gap:10px}
.socials{display:flex;gap:10px;margin-top:6px}
.socials span{width:14px;height:14px;border-radius:50%;background:#bbb}
.newsletter{position:absolute;left:330px;top:221px;display:flex;align-items:center}
.newsletter label{font-size:17px;color:var(--white);width:127px}
.newsletter .field{width:547px;height:34px;background:var(--white);font-size:10px;color:#999;padding:10px 12px}
.newsletter .submit{width:94px;height:34px;background:var(--red);color:var(--white);font-size:12px;font-weight:600;display:flex;align-items:center;justify-content:center}
.bottom-bar{position:absolute;top:3762px;left:0;width:1200px;height:52px;background:var(--grey-deep);color:#bbb;font-size:10px}
.bottom-bar .copy{position:absolute;left:97px;top:19px}
.bottom-bar .links{position:absolute;right:90px;top:19px;display:flex;gap:26px}
</style>
</head>
<body>
<div class="page">

  <header class="hero">
    <div class="hero-shade" role="img" aria-label="Photograph of a modern glass office building under a clear sky"></div>
    <div class="topbar">
      <div class="brand">
        <div class="brand-mark"></div>
        <div>
          <div class="brand-name">Veltrane Partners</div>
          <div class="brand-tag">IIoT Strategy. Sensor Innovation. Machine Learning</div>
        </div>
      </div>
      <nav class="nav">
        <span class="active">HOME</span><span>ABOUT US</span><span>SERVICES</span><span>EVENTS</span><span>BLOG</span><span>CONTACT US</span>
      </nav>
      <svg class="search-icon" viewBox="0 0 22 22"><circle cx="11" cy="11" r="10" fill="none" stroke="#fff" stroke-width="1.2"/><circle cx="10" cy="10" r="4" fill="none" stroke="#fff" stroke-width="1.4"/><line x1="13" y1="13" x2="16" y2="16" stroke="#fff" stroke-width="1.4"/></svg>
      <div class="search-box"></div>
    </div>
    <h1>Veltrane Partners are Innovators, Engineers</h1>
    <div class="hero-sub">Donec tincidunt dapibus erat, vel pharetra turpis. Praesent tincidunt mi et sapien condimentum euismod sed eget odio.</div>
    <div class="btn btn-hero">Get in touch <span class="arrow"><svg width="10" height="10" viewBox="0 0 10 10"><path d="M3 1l4 4-4 4" fill="none" stroke="#222" stroke-width="2"/></svg></span></div>
  </header>

  <section class="about">
    <h2 class="sec-title" style="top:62px">About Veltrane Partners</h2>
    <div class="sec-rule" style="top:112px"></div>
    <p style="top:140px">The core team at Veltrane Partners are Innovators, Engineers, PhDs and Data Scientists who assist mid-sized companies ($25M- $500M) to capitalise on the enormous potential of the Industrial Internet of Things ("IIoT").</p>
    <p style="top:196px">Our three business units – Strategy, Sensors and AI – mean that we can provide expert advice to both new entrants and companies already familiar with IIoT.</p>
    <p style="top:252px">Founded by our Chief Strategy Officer and serial entrepreneur, Tam Verrow, Veltrane is based in London and have plans to open offices in Tokyo and LA in late 2017.</p>
    <div class="btn btn-small" style="left:524px;top:324px">Read more <span class="arrow"><svg width="8" height="8" viewBox="0 0 10 10"><path d="M3 1l4 4-4 4" fill="none" stroke="#222" stroke-width="2"/></svg></span></div>
  </section>

  <section class="strategy" role="img" aria-label="Dark photograph of city office towers behind the strategy text">
    <h2 class="sec-title" style="top:20px">Our Strategy</h2>
    <div class="sec-rule" style="top:66px"></div>
    <p style="top:94px">The Strategy team work with customers to navigate the complex world of IIoT and develop world-class strategies for maximising value. We know that connecting assets is not appropriate for every business: sometimes the challenges outweigh the rewards.</p>
    <p style="top:180px">However, where an IIoT strategy is appropriate we have the right team to help your company clarify its visions, goals &amp; guiding principles and manage the IIoT roadmap in partnership with your senior team.</p>
    <div class="ideas">Ideas for IIoT strategy development include:</div>
    <div class="idea" style="left:127px">Opportunities for quality &amp; maintenance improvements</div>
    <div class="idea" style="left:364px">Potential for offering new services to customers</div>
    <div class="idea" style="left:601px">Investigating new data, service or product-centric business models</div>
    <div class="idea" style="left:838px">Developing new revenue streams</div>
  </section>

  <section class="sensors">
    <h2>Sensors</h2>
    <p>The Sensor team are focused on innovation using Sensors and MEMS (Micro-Electromechanical Systems.) We view ourselves as the conduit between the vast array of complex sensors and their potential applications in the "real world."</p>
    <div class="btn btn-small" style="left:100px;top:384px">Read more <span class="arrow"><svg width="8" height="8" viewBox="0 0 10 10"><path d="M3 1l4 4-4 4" fill="none" stroke="#222" stroke-width="2"/></svg></span></div>

    <svg class="sensor-tree" viewBox="0 0 1200 560" font-family="Open Sans, Arial, sans-serif" font-weight="700" font-size="14" fill="#fff" text-anchor="middle">
      <g stroke="#9a9a9a" stroke-width="3" fill="none">
        <line x1="745" y1="280" x2="790" y2="280"/>
        <line x1="790" y1="70" x2="790" y2="490"/>
        <line x1="790" y1="70" x2="820" y2="70"/><line x1="790" y1="112" x2="820" y2="112"/>
        <line x1="790" y1="154" x2="820" y2="154"/><line x1="790" y1="196" x2="820" y2="196"/>
        <line x1="790" y1="238" x2="820" y2="238"/><line x1="790" y1="280" x2="820" y2="280"/>
        <line x1="790" y1="322" x2="820" y2="322"/><line x1="790" y1="364" x2="820" y2="364"/>
        <line x1="790" y1="406" x2="820" y2="406"/><line x1="790" y1="448" x2="820" y2="448"/>
        <line x1="790" y1="490" x2="820" y2="490"/>
      </g>
      <circle cx="640" cy="280" r="105" fill="#e2231a" stroke="#fff" stroke-width="10"/>
      <text x="640" y="293" font-size="36">Sensors</text>
      <g fill="#4a4a4a">
        <rect x="820" y="53" width="290" height="34" rx="17"/><rect x="820" y="95" width="290" height="34" rx="17"/>
        <rect x="820" y="137" width="290" height="34" rx="17"/><rect x="820" y="179" width="290" height="34" rx="17"/>
        <rect x="820" y="221" width="290" height="34" rx="17"/><rect x="820" y="263" width="290" height="34" rx="17"/>
        <rect x="820" y="305" width="290" height="34" rx="17"/><rect x="820" y="347" width="290" height="34" rx="17"/>
        <rect x="820" y="389" width="290" height="34" rx="17"/><rect x="820" y="431" width="290" height="34" rx="17"/>
        <rect x="820" y="473" width="290" height="34" rx="17"/>
      </g>
      <text x="965" y="75">Motion / Velocity</text>
      <text x="965" y="117">Acceleration / Tilt</text>
      <text x="965" y="159">Levels &amp; Leaks</text>
      <text x="965" y="201">Temperature</text>
      <text x="965" y="243">Moisture &amp; Humidity</text>
      <text x="965" y="285">Pressure / Force / Load</text>
      <text x="965" y="327">Water / Liquid Flow</text>
      <text x="965" y="369">Sound / Vibration</text>
      <text x="965" y="411">Proximity / Presence / Position</text>
      <text x="965" y="453">Machine Vision</text>
      <text x="965" y="495">Chemical and gas</text>
    </svg>
  </section>

  <section class="data" role="img" aria-label="Dark photograph of hands typing on a laptop keyboard">
    <h2>Data &amp; AI</h2>
    <p>The Data &amp; AI team focus on getting the maximum value from our customer's sensors. We are a small team of engineers and data scientists who know that the real value from IIoT comes from the quality of sensor data. We monitor and analyse this data and then deliver it to our customers via stunning dashboards.</p>
    <div class="pill" style="left:96px">Rich Data</div>
    <div class="pill red" style="left:302px">Realtime<br>Analytics</div>
    <div class="pill" style="left:505px">Historical<br>Analytics</div>
    <div class="pill red" style="left:706px">Predictive<br>Analitics</div>
    <div class="pill" style="left:910px">Intelligent<br>Decision<br>Making</div>
    <div class="outline-btn">Sensors</div>
  </section>

  <section class="events">
    <div class="kicker" style="left:110px;top:40px">Latest</div>
    <div class="big-label" style="left:108px;top:60px">Events</div>
    <div class="event-photo" role="img" aria-label="Photograph of a seminar audience in a warmly lit hall facing a presentation screen"></div>
    <div class="event-head">UPCOMING EVENTS</div>
    <div class="event-note">INTEGER NISI ROBOT MI VEL FERMENTUM</div>
    <div class="cal">
      <div class="cal-top"><span>March 2017</span><span class="dots">‹ ›</span></div>
      <table>
        <tr><th>SUN</th><th>MON</th><th>TUE</th><th>WED</th><th>THU</th><th>FRI</th><th>SAT</th></tr>
        <tr><td></td><td></td><td></td><td>1</td><td>2</td><td>3</td><td>4</td></tr>
        <tr><td>5</td><td>6</td><td>7</td><td>8</td><td class="today"><span>9</span></td><td>10</td><td>11</td></tr>
        <tr><td>12</td><td>13</td><td>14</td><td>15</td><td>16</td><td>17</td><td>18</td></tr>
        <tr><td>19</td><td>20</td><td>21</td><td>22</td><td>23</td><td>24</td><td>25</td></tr>
        <tr><td>26</td><td>27</td><td>28</td><td>29</td><td>30</td><td>31</td><td></td></tr>
      </table>
    </div>
    <div class="tree" role="img" aria-label="Faint pine tree decoration"></div>
    <div class="view-all">VIEW ALL EVENTS</div>
    <ul class="event-list">
      <li>LOREM IPSUM DOLOR SIT AMET<small>MARCH 21, 2016</small></li>
      <li>DONEC POSUERE NUNC DOLOR TEMPOR<small>MARCH 21, 2016</small></li>
      <li>VESTIBULUM SIT AMET VESTIBULUM DIAM<small>MARCH 21, 2016</small></li>
      <li>QUISQUE SIT AMET DIAM QUIS<small>MARCH 21, 2016</small></li>
    </ul>
  </section>

  <section class="blogs">
    <div class="kicker" style="left:118px;top:35px">Latest</div>
    <div class="big-label" style="left:118px;top:55px">Blogs</div>
    <article class="card" style="left:119px"><div class="card-photo" role="img" aria-label="Photograph of a woman working at a laptop in a bright office" style="background:linear-gradient(135deg,#d9d4cc,#9a8f84)"></div><time>October 20, 2016</time><h3>Nam dictum est neque, nec pretium tortor tincidunt in.</h3></article>
    <article class="card" style="left:363px"><div class="card-photo" role="img" aria-label="Photograph of colleagues discussing plans around a table" style="background:linear-gradient(135deg,#8b7867,#4f463f)"></div><time>October 20, 2016</time><h3>Nam dictum est neque, nec pretium tortor tincidunt in.</h3></article>
    <article class="card" style="left:608px"><div class="card-photo" role="img" aria-label="Photograph of a team meeting in a modern workspace" style="background:linear-gradient(135deg,#e3ddd2,#a59787)"></div><time>October 20, 2016</time><h3>Nam dictum est neque, nec pretium tortor tincidunt in.</h3></article>
    <article class="card" style="left:854px"><div class="card-photo" role="img" aria-label="Photograph of a smiling man in a casual shirt" style="background:linear-gradient(135deg,#6f6a66,#b4a290)"></div><time>October 20, 2016</time><h3>Nam dictum est neque, nec pretium tortor tincidunt in.</h3></article>
  </section>

  <footer class="footer">
    <div class="foot-brand">
      <div class="mark"></div>
      <div class="name">Veltrane Partners</div>
      <div class="tag">IIoT Strategy Sensor Innovation Machine Learning</div>
    </div>
    <div class="foot-col" style="left:348px">
      <h4>Products</h4>
      Home<br>About Us<br>Services<br>Events<br>Blog
    </div>
    <div class="foot-col" style="left:640px">
      <h4>Norvanta Inc.</h4>
      <div class="contact-row"><svg width="10" height="14" viewBox="0 0 10 14"><path d="M5 0a5 5 0 0 0-5 5c0 4 5 9 5 9s5-5 5-9a5 5 0 0 0-5-5z" fill="#ccc"/></svg><span style="line-height:1.4">124 Sed mollis consequat nibh ac<br>consectetur USA</span></div>
      <div class="contact-row" style="margin-top:8px"><svg width="12" height="10" viewBox="0 0 12 10"><rect x=".5" y=".5" width="11" height="9" fill="none" stroke="#ccc"/><path d="M.5 .5l5.5 5 5.5-5" fill="none" stroke="#ccc"/></svg><span>info@veltranepartners.com</span></div>
      <div class="contact-row"><svg width="12" height="12" viewBox="0 0 12 12"><path d="M2 1l3 1-1 2a7 7 0 0 0 4 4l2-1 1 3-2 1C5 11 1 7 1 3z" fill="#ccc"/></svg><span>+91 900 555 0142</span></div>
    </div>
    <div class="foot-col" style="left:984px">
      <h4>News &amp; Events</h4>
      Events<br>Press Releases<br>Blog
      <div class="socials"><span></span><span></span><span></span><span></span></div>
    </div>
    <div class="newsletter">
      <label>Newsletter</label>
      <div class="field">Email Address</div>
      <div class="submit">Sign up</div>
    </div>
  </footer>
  <div class="bottom-bar">
    <div class="copy">© 2017 Veltrane Partners . All Rights Reserved.</div>
    <div class="links"><span>Terms of Use</span><span>Contact Veltrane Partners</span><span>English</span><span>UK</span></div>
  </div>

</div>
</body>
</html>
```